Business Card Trio Design

We need a set of business cards that all match but are not identical. We need one generic for the business and one for each of the two owners. We would like the cards to be similar to each other, but not identical. We have a logo and the colors of the logo are painstakingly chosen so if blue or green is used, we prefer our specific blue and green. Our logo pops better on a black background as well. We are open to double-sided, but it is not the top choice. We would love some either gold or silver accents that are in a foiled appearance. We sell uniforms (scrubs, culinary, EMT, police, fire, business, all types except kids and sports), shoes, equipment, and accessories. We also have facebook, pinterest, instagram, and twitter that we would like to have them follow and we offer splitwell in the store we would like the card to also advertise.

```html
<!DOCTYPE html>
<html lang="en">
<head>
<meta charset="utf-8">
<title>Verdant Uniforms – Business Card</title>
<link href="https://fonts.googleapis.com/css2?family=Montserrat:wght@300;400;500&display=swap" rel="stylesheet">
<style>
  :root {
    --stage: #141414;
    --card-dark: #222222;
    --card-dark-back: #262626;
    --card-light: #ffffff;
    --brand-blue: #7a9ec2;
    --brand-green: #12966f;
    --text-grey: #4a4a4a;
    --icon-grey: #a8a8a8;
    --rule-grey: #8c8c8c;
  }
  * { box-sizing: border-box; margin: 0; padding: 0; }
  html, body { width: 1200px; height: 1200px; overflow: hidden; }
  body {
    background: var(--stage);
    font-family: "Montserrat", sans-serif;
    position: relative;
  }
  .card {
    position: absolute;
    left: 250px;
    width: 700px;
    height: 400px;
    border-radius: 22px;
    overflow: hidden;
  }
  .card--front { top: 173px; background: var(--card-dark); }
  .card--back { top: 627px; background: var(--card-dark-back); }
  .card__art { position: absolute; inset: 0; width: 100%; height: 100%; }

  .brand-mark {
    position: absolute;
    text-align: center;
    color: var(--brand-blue);
    font-weight: 500;
    line-height: 1;
    text-transform: uppercase;
  }
  .brand-mark__dot {
    display: block;
    margin: 0 auto 14px;
    border-radius: 50%;
    background: var(--brand-green);
  }
  .card--front .brand-mark { left: 63px; top: 45px; width: 200px; }
  .card--front .brand-mark__dot { width: 70px; height: 70px; }
  .card--front .brand-mark__name { font-size: 31px; letter-spacing: 1px; }
  .card--front .brand-mark__line { font-size: 23px; letter-spacing: 6px; margin-top: 4px; }

  .contact {
    position: absolute;
    right: 39px;
    top: 206px;
    text-align: right;
  }
  .contact__name {
    font-size: 26px;
    font-weight: 500;
    color: var(--brand-blue);
    letter-spacing: 0.3px;
  }
  .contact__role {
    font-size: 17px;
    font-weight: 400;
    color: var(--brand-green);
    margin-top: 2px;
  }
  .contact__list { list-style: none; margin-top: 18px; }
  .contact__item {
    display: flex;
    justify-content: flex-end;
    align-items: center;
    gap: 9px;
    font-size: 15px;
    font-weight: 300;
    color: var(--text-grey);
    height: 22.5px;
  }
  .contact__icon { width: 12px; height: 12px; flex: none; }

  .back-disc {
    position: absolute;
    left: 17px;
    top: 23px;
    width: 360px;
    height: 360px;
    border-radius: 50%;
    background: radial-gradient(circle at 30% 30%, #5e5e5e, #2e2e2e 75%);
  }
  .card--back .brand-mark { left: 410px; top: 256px; width: 228px; }
  .card--back .brand-mark__name { font-size: 37px; letter-spacing: 1px; }
  .card--back .brand-mark__line { font-size: 27px; letter-spacing: 7px; margin-top: 4px; }
  .social {
    position: absolute;
    left: 411px;
    top: 335px;
    width: 224px;
    display: flex;
    align-items: center;
    gap: 8px;
  }
  .social__rule { flex: 1; height: 1px; background: var(--rule-grey); }
  .social__spot { width: 24px; height: 24px; border-radius: 50%; background: var(--icon-grey); }
</style>
</head>
<body>

<section class="card card--front" aria-label="Business card front">
  <svg class="card__art" viewBox="0 0 1050 600" preserveAspectRatio="none" aria-hidden="true">
    <path fill="var(--brand-blue)" d="M650,212 C760,150 900,130 1050,205 L1050,242 C920,175 800,160 650,212 Z"/>
    <path fill="var(--brand-green)" d="M0,400 C110,460 230,470 348,420 C230,478 100,475 0,445 Z"/>
    <path fill="var(--card-light)" d="M0,455 C150,515 300,470 450,380 C600,280 700,175 830,180 C930,184 1000,228 1050,255 L1050,600 L0,600 Z"/>
  </svg>

  <div class="brand-mark">
    <span class="brand-mark__dot"></span>
    <div class="brand-mark__name">Verdant</div>
    <div class="brand-mark__line">Uniforms</div>
  </div>

  <div class="contact">
    <div class="contact__name">JORDAN HALE</div>
    <div class="contact__role">Owner</div>
    <ul class="contact__list">
      <li class="contact__item">(555) 014-2231
        <svg class="contact__icon" viewBox="0 0 12 12"><rect x="2.5" y="0.8" width="7" height="10.4" rx="1.2" fill="none" stroke="var(--brand-green)" stroke-width="1.4"/><circle cx="6" cy="9.3" r="0.7" fill="var(--brand-green)"/></svg>
      </li>
      <li class="contact__item">(555) 019-0711
        <svg class="contact__icon" viewBox="0 0 12 12"><rect x="2.5" y="0.8" width="7" height="10.4" rx="1.2" fill="none" stroke="var(--brand-green)" stroke-width="1.4"/><circle cx="6" cy="9.3" r="0.7" fill="var(--brand-green)"/></svg>
      </li>
      <li class="contact__item">verdantuniformshop@mail.com
        <svg class="contact__icon" viewBox="0 0 12 12"><rect x="0.5" y="2.5" width="11" height="7.5" fill="var(--brand-green)"/><path d="M0.8,2.8 L6,7 L11.2,2.8" fill="none" stroke="#fff" stroke-width="0.9"/></svg>
      </li>
      <li class="contact__item">www.verdantuniforms.com
        <svg class="contact__icon" viewBox="0 0 12 12"><circle cx="6" cy="6" r="5.5" fill="var(--brand-green)"/><path d="M3,3.5 C4.5,3 5,4.5 4,5.5 C3.5,6.5 5,7 5,8.5 M7.5,2 C7,3.5 8.5,4 9.5,4.5 M7.5,7.5 C8.5,7 9.5,8 8.5,9.5" fill="none" stroke="#fff" stroke-width="1"/></svg>
      </li>
    </ul>
  </div>
</section>

<section class="card card--back" aria-label="Business card back">
  <div class="back-disc" role="img" aria-label="Large embossed brand emblem"></div>

  <div class="brand-mark">
    <div class="brand-mark__name">Verdant</div>
    <div class="brand-mark__line">Uniforms</div>
  </div>

  <div class="social" aria-label="Social media">
    <span class="social__rule"></span>
    <span class="social__spot"></span>
    <span class="social__spot"></span>
    <span class="social__spot"></span>
    <span class="social__rule"></span>
  </div>
</section>

</body>
</html>
```